Venture Capital Firm Needs Website Redesign

We need a bold revamp of our website (https://halvenmoor.vc/)
which at the moment looks washed out. We want a crisp, fresh and unique look. Feel free to keep as much or as little content in the site. The only thing we need to keep is a team section. The site should convey a clear distinction between our 3 product lines: Venture Capital, Private Credit, and Crypto. Two versions of our logo are attached and they should not change. For design inspirations, we like http://www.plumridgecap.com/ for a more simple site and for a more built out site we like http://tallowgate.com/

Updates
Industry/Entity Type
Investment
Coding
Coded - Design and coding required
Number of Pages Required
1 page
Font styles to use
Colors
Designer to choose colors to be used in the design.
Requirements
Must have
- - Clear distinction between our 3 product lines: Venture Capital, Private Credit
- - Team section

Nice to have
- Some really creative aspect like http://www.plumridgecap.com/ has with the distinction between first, second, and third kind

```html
<!DOCTYPE html>
<html lang="en">
<head>
<meta charset="utf-8">
<title>Halvenmoor</title>
<link href="https://fonts.googleapis.com/css2?family=Roboto:wght@300;400;500;700&family=Open+Sans:wght@400;600;700&display=swap" rel="stylesheet">
<style>
:root{
  --green:#8fa832;
  --green-dark:#7d9429;
  --ink:#2b2b2b;
  --text:#4a4a4a;
  --muted:#777;
  --light:#f5f5f5;
  --white:#ffffff;
  --card:#3b3b3b;
  --footer:#333333;
  --line:#e2e2e2;
}
*{box-sizing:border-box;margin:0;padding:0}
html,body{width:1200px;height:3629px;overflow:hidden}
body{position:relative;background:var(--white);font-family:"Open Sans",Arial,sans-serif;color:var(--text)}
.abs{position:absolute}
.section{position:absolute;left:0;width:1200px}
.btn{position:absolute;background:var(--green);color:var(--white);font-family:"Open Sans",Arial,sans-serif;font-size:13px;font-weight:600;display:flex;align-items:center;justify-content:center;border-radius:20px;height:36px}
.brand{font-family:"Roboto",Arial,sans-serif;font-weight:400;font-size:42px;letter-spacing:1px;color:var(--ink)}
/* hero */
.hero{top:0;height:770px;background:linear-gradient(135deg,#f4f4f4 0%,#e6e6e6 45%,#f7f7f7 100%)}
.hero-visual{position:absolute;inset:0;background:radial-gradient(circle at 60% 45%,rgba(255,255,255,.9) 0%,rgba(230,230,230,.6) 35%,rgba(215,215,215,.4) 60%,rgba(245,245,245,.8) 100%)}
.menu{position:absolute;left:1045px;top:82px;width:34px}
.menu span{display:block;height:4px;background:var(--ink);margin-bottom:6px;border-radius:2px}
.hero-title{position:absolute;top:318px;width:1200px;text-align:center;font-family:"Open Sans",sans-serif;font-weight:700;font-size:37px;color:var(--ink)}
.hero-title em{font-style:normal;color:var(--green)}
.hero-sub{position:absolute;top:362px;width:1200px;text-align:center;font-family:"Open Sans",sans-serif;font-weight:600;font-size:21px;line-height:31px;color:var(--ink)}
/* product sections */
.sec-title{position:absolute;font-family:"Roboto",sans-serif;font-weight:300;font-size:33px;color:var(--ink);letter-spacing:.5px}
.sec-title em{font-style:normal;color:var(--green)}
.sec-text{position:absolute;font-size:13.5px;line-height:20px;color:var(--text)}
.partner{position:absolute;width:116px;height:80px;border:1px solid var(--line);background:var(--white);display:flex;align-items:center;justify-content:center;font-family:"Roboto",sans-serif;font-size:16px;color:#3c4d8a}
.partner.wide{width:140px;height:78px;font-size:19px;color:#3a3a3a}
.illus{position:absolute;border-radius:50%;background:radial-gradient(circle,#eef2dc 0%,#f7f9ef 60%,rgba(255,255,255,0) 72%)}
.credit{top:1311px;height:547px;background:var(--light)}
.credit .illus{background:radial-gradient(circle,#e8edd2 0%,#eff2e2 60%,rgba(245,245,245,0) 72%)}
/* team */
.team{top:2351px;height:620px;background:var(--light)}
.team-title{position:absolute;top:86px;width:1200px;text-align:center;font-family:"Roboto",sans-serif;font-weight:300;font-size:33px;color:var(--ink)}
.team-title em{font-style:normal;color:var(--green)}
.team-sub{position:absolute;top:126px;width:1200px;text-align:center;font-size:13px;color:var(--text)}
.arrow{position:absolute;top:87px;width:28px;height:28px;border-radius:50%;display:flex;align-items:center;justify-content:center}
.card{position:absolute;top:189px;width:218px;height:249px;background:var(--card);border-radius:6px;text-align:center}
.card.active{background:var(--green)}
.portrait{position:absolute;left:47px;top:16px;width:124px;height:124px;border-radius:50%;background:linear-gradient(160deg,#d9d9d9,#a9a9a9);border:4px solid var(--white)}
.card-name{position:absolute;top:160px;width:218px;font-family:"Roboto",sans-serif;font-weight:700;font-size:19px;color:var(--green)}
.card.active .card-name{color:var(--white)}
.card-role{position:absolute;top:186px;width:218px;font-size:8px;font-weight:700;color:var(--white);letter-spacing:.5px}
.socials{position:absolute;top:205px;width:218px;display:flex;justify-content:center;gap:6px}
.dot{width:24px;height:24px;border-radius:50%;background:var(--white)}
/* newsletter */
.news{top:2971px;height:258px;background:var(--white)}
.news-title{position:absolute;top:80px;width:1200px;text-align:center;font-family:"Roboto",sans-serif;font-weight:400;font-size:22px;color:var(--ink);letter-spacing:.5px}
.news-title em{font-style:normal;color:var(--green)}
.news-sub{position:absolute;top:109px;width:1200px;text-align:center;font-size:13px;color:var(--text)}
.news-form{position:absolute;left:314px;top:150px;width:552px;height:36px;border-radius:18px;background:var(--light);display:flex;align-items:center}
.news-form span{padding-left:28px;font-size:13px;color:var(--muted);flex:1}
.news-form b{width:126px;height:36px;border-radius:18px;background:var(--green);color:var(--white);display:flex;align-items:center;justify-content:center;font-size:14px;font-weight:700}
/* footer */
.footer{top:3229px;height:351px;background:var(--footer);color:var(--white)}
.footer .brand{color:var(--white);font-size:40px}
.f-head{position:absolute;top:70px;font-family:"Roboto",sans-serif;font-weight:700;font-size:13px;color:var(--white)}
.f-head::after{content:"";display:block;width:24px;height:2px;background:var(--green);margin-top:5px}
.f-text{position:absolute;font-size:13px;line-height:17px;color:#e4e4e4}
.f-list{position:absolute;top:137px;left:438px;list-style:none;font-size:13px;line-height:17.5px;color:#e4e4e4}
.f-list li::before{content:"• ";color:#e4e4e4}
.f-input{position:absolute;background:var(--white);border-radius:10px;height:22px;font-size:11px;color:#999;padding:3px 10px}
.bar{top:3580px;height:49px;background:var(--green);color:var(--white)}
.bar p{position:absolute;left:121px;top:15px;font-size:14px}
.bar .icons{position:absolute;left:904px;top:12px;display:flex;gap:12px}
.bar .icons span{width:25px;height:25px;border-radius:50%;background:var(--white)}
</style>
</head>
<body>

<header class="section hero">
  <div class="hero-visual" role="img" aria-label="Soft grey photograph of a spiral staircase seen from below"></div>
  <div class="brand abs" style="left:119px;top:70px">HALVENMOOR</div>
  <div class="menu" aria-label="Menu"><span></span><span></span><span></span></div>
  <h1 class="hero-title"><em>HALVENMOOR</em> OPERATES</h1>
  <p class="hero-sub">AT THE INTERSECTION OF TECHNOLOGY AND<br>NOVEL ASSET CLASSES.</p>
  <a class="btn" style="left:520px;top:432px;width:160px">Read More</a>
</header>

<section class="section venture" style="top:770px;height:541px">
  <h2 class="sec-title" style="left:121px;top:98px"><em>VENTURE</em> CAPITAL</h2>
  <p class="sec-text" style="left:121px;top:160px;width:490px">We invest in early-stage startups led by founders who are passionate and knowledgeable about the markets they serve. We have our own software developers and product managers. We work with the founders in our portfolio to help them bring products to market, earning equity for this work and for the cash we invest in their companies..</p>
  <a class="btn" style="left:121px;top:282px;width:157px">Read More</a>
  <div class="partner" style="left:121px;top:367px">Norbrook</div>
  <div class="partner" style="left:242px;top:367px;color:#6a4a8a">lumacode</div>
  <div class="partner" style="left:363px;top:367px;color:#2a8fd0">tinyroam</div>
  <div class="partner" style="left:484px;top:367px;color:#2f3f6a">Fernstitch</div>
  <div class="illus" role="img" aria-label="Line illustration of a hand holding a money bag with a dollar sign" style="left:742px;top:108px;width:280px;height:280px"></div>
</section>

<section class="section credit">
  <div class="illus" role="img" aria-label="Line illustration of a fist gripping a money bag with a dollar sign" style="left:206px;top:146px;width:290px;height:260px"></div>
  <h2 class="sec-title" style="left:636px;top:82px"><em>PRIVATE</em> CREDIT</h2>
  <p class="sec-text" style="left:636px;top:140px;width:450px">Halvenmoor Private Credit provides capital to lending businesses that are focused on using technology to establish new credit markets, create new credit products or dramatically re-invent an existing form of credit.&nbsp; We believe that the pioneers who build something truly different in a credit market will create the most sustainable business models.&nbsp; Given our heritage as a venture firm, we are comfortable with emerging businesses and can provide capital for a company's first loan.</p>
  <a class="btn" style="left:636px;top:297px;width:131px">Read More</a>
  <div class="partner wide" style="left:636px;top:363px;color:#1f3f8a">Corvale</div>
  <div class="partner wide" style="left:784px;top:363px"><span style="width:34px;height:34px;border-radius:50%;background:#7a8a5a;display:block"></span></div>
  <div class="partner wide" style="left:931px;top:363px">Brightledger</div>
</section>

<section class="section crypto" style="top:1858px;height:493px">
  <h2 class="sec-title" style="left:121px;top:117px"><em>CRYPTO</em> INDEX</h2>
  <p class="sec-text" style="left:121px;top:178px;width:470px">The Halvenmoor Crypto Index tracks the top 15 cryptocurrencies weighted by market cap and rebalanced twice a month. We believe this is the simplest and most cost effective way to obtain cryptocurrency exposure. Our process has been designed by experts from financial services and cryptocurrency industries.</p>
  <a class="btn" style="left:126px;top:282px;width:157px">Read More</a>
  <svg class="abs" style="left:634px;top:77px" width="443" height="315" viewBox="0 0 443 315" font-family="Roboto, sans-serif">
    <text x="221" y="12" font-size="10" text-anchor="middle" fill="#555">HCI™ Cumulative Growth</text>
    <circle cx="95" cy="27" r="6" fill="#a9b83a"/><text x="106" y="31" font-size="9" fill="#555">HCI™ (1236.40%)</text>
    <circle cx="200" cy="27" r="6" fill="#111"/><text x="211" y="31" font-size="9" fill="#555">Benchmark (717.41%)</text>
    <g stroke="#e6e6e6" stroke-width="1">
      <line x1="45" y1="55" x2="430" y2="55"/><line x1="45" y1="85" x2="430" y2="85"/><line x1="45" y1="115" x2="430" y2="115"/><line x1="45" y1="145" x2="430" y2="145"/><line x1="45" y1="175" x2="430" y2="175"/><line x1="45" y1="205" x2="430" y2="205"/><line x1="45" y1="235" x2="430" y2="235"/><line x1="45" y1="265" x2="430" y2="265"/>
      <line x1="45" y1="55" x2="45" y2="265"/><line x1="77" y1="55" x2="77" y2="265"/><line x1="109" y1="55" x2="109" y2="265"/><line x1="141" y1="55" x2="141" y2="265"/><line x1="173" y1="55" x2="173" y2="265"/><line x1="205" y1="55" x2="205" y2="265"/><line x1="237" y1="55" x2="237" y2="265"/><line x1="269" y1="55" x2="269" y2="265"/><line x1="301" y1="55" x2="301" y2="265"/><line x1="333" y1="55" x2="333" y2="265"/><line x1="365" y1="55" x2="365" y2="265"/><line x1="397" y1="55" x2="397" y2="265"/><line x1="429" y1="55" x2="429" y2="265"/>
    </g>
    <g font-size="9" fill="#666" text-anchor="end">
      <text x="38" y="58">3500</text><text x="38" y="88">3000</text><text x="38" y="118">2500</text><text x="38" y="148">2000</text><text x="38" y="178">1500</text><text x="38" y="208">1000</text><text x="38" y="238">500</text><text x="38" y="268">0</text>
    </g>
    <g font-size="9" fill="#666" text-anchor="end">
      <text transform="translate(48,275) rotate(-90)">Jan</text><text transform="translate(80,275) rotate(-90)">Feb</text><text transform="translate(112,275) rotate(-90)">Mar</text><text transform="translate(144,275) rotate(-90)">Apr</text><text transform="translate(176,275) rotate(-90)">May</text><text transform="translate(208,275) rotate(-90)">Jun</text><text transform="translate(240,275) rotate(-90)">Jul</text><text transform="translate(272,275) rotate(-90)">Aug</text><text transform="translate(304,275) rotate(-90)">Sep</text><text transform="translate(336,275) rotate(-90)">Oct</text><text transform="translate(368,275) rotate(-90)">Nov</text><text transform="translate(400,275) rotate(-90)">Dec</text><text transform="translate(432,275) rotate(-90)">Jan</text>
    </g>
    <polyline fill="none" stroke="#a9b83a" stroke-width="2.5" points="45,265 61,263.8 77,263.2 93,261.4 109,257.8 125,253 141,242.2 157,247 173,236.2 189,239.8 205,226 221,235 237,229 253,233.8 269,223 285,217 301,205 317,193 333,175 349,139 365,85 381,127 397,121 413,151 429,175"/>
    <polyline fill="none" stroke="#111" stroke-width="2.5" points="45,265 61,264.4 77,263.8 93,262.6 109,259.6 125,256 141,248.2 157,251.8 173,244 189,247 205,238 221,242.2 237,239.8 253,241 269,235 285,233 301,229 317,223 333,211 349,193 365,163 381,181 397,175 413,199 429,205"/>
  </svg>
</section>

<section class="section team">
  <h2 class="team-title"><em>OUR</em> TEAM</h2>
  <p class="team-sub">The very best helping the very best.</p>
  <span class="arrow" style="left:1016px;background:#333"><svg width="12" height="12" viewBox="0 0 12 12"><path d="M8 2 L4 6 L8 10" stroke="#fff" stroke-width="2" fill="none"/></svg></span>
  <span class="arrow" style="left:1051px;background:var(--green)"><svg width="12" height="12" viewBox="0 0 12 12"><path d="M4 2 L8 6 L4 10" stroke="#fff" stroke-width="2" fill="none"/></svg></span>

  <article class="card" style="left:121px">
    <div class="portrait" role="img" aria-label="Portrait photo of team partner"></div>
    <h3 class="card-name">OMAR SELDEN</h3><p class="card-role">PARTNER</p>
    <div class="socials"><span class="dot"></span><span class="dot"></span><span class="dot"></span></div>
  </article>
  <article class="card active" style="left:368px">
    <div class="portrait" role="img" aria-label="Portrait photo of team partner"></div>
    <h3 class="card-name">RAVI TANDELL</h3><p class="card-role">PARTNER</p>
    <div class="socials"><span class="dot"></span><span class="dot"></span><span class="dot"></span></div>
  </article>
  <article class="card" style="left:614px">
    <div class="portrait" role="img" aria-label="Portrait photo of team partner"></div>
    <h3 class="card-name">KARIM ASHVALE</h3><p class="card-role">PARTNER</p>
    <div class="socials"><span class="dot"></span><span class="dot"></span><span class="dot"></span></div>
  </article>
  <article class="card" style="left:861px">
    <div class="portrait" role="img" aria-label="Portrait photo of team partner"></div>
    <h3 class="card-name">WALKER FENN</h3><p class="card-role">PARTNER</p>
    <div class="socials"><span class="dot"></span><span class="dot"></span><span class="dot"></span></div>
  </article>

  <a class="btn" style="left:520px;top:493px;width:160px;height:38px">View More</a>
</section>

<section class="section news">
  <h2 class="news-title"><em>SUBSCRIBE</em> TO OUR NEWSLETTER</h2>
  <p class="news-sub">To Receive The latest News And Update</p>
  <div class="news-form"><span>Your E-Mail</span><b>SUBMIT</b></div>
</section>

<footer class="section footer">
  <div class="brand abs" style="left:121px;top:52px">HALVENMOOR</div>
  <p class="f-text" style="left:121px;top:133px;width:260px">Lorem Ipsum is simply dummy text of the printing and typesetting indu stry. Lorem text of the printing and typesett Ipsum industries.</p>
  <p class="f-text" style="left:121px;top:212px">Read More.. <span style="display:inline-block;width:10px;height:10px;border-radius:50%;background:var(--green)"></span></p>

  <h4 class="f-head" style="left:438px">QUICK LINKS</h4>
  <ul class="f-list"><li>Venture</li><li>Private Credit</li><li>Crypto</li><li>Halvenmoor</li><li>About us</li><li>Team</li><li>Blog</li></ul>

  <h4 class="f-head" style="left:605px">CONTACT US</h4>
  <p class="f-text" style="left:605px;top:137px;line-height:21px">218 Calder Street, Suite 410<br>New York,<br>NY 10012<br>+1 555 014 2283<br>info@halvenmoor.vc</p>

  <h4 class="f-head" style="left:854px">QUICK CONTACT</h4>
  <div class="f-input" style="left:854px;top:146px;width:112px">Name</div>
  <div class="f-input" style="left:970px;top:146px;width:112px">Phone</div>
  <div class="f-input" style="left:854px;top:172px;width:228px;height:46px">Message</div>
  <div class="btn" style="left:965px;top:232px;width:117px;height:24px;font-size:11px;font-weight:400">Send</div>
</footer>

<div class="section bar">
  <p>Copyright © 2018 HALVENMOOR.&nbsp; All Rights Reserved.</p>
  <div class="icons"><span></span><span></span><span></span><span></span><span></span></div>
</div>

</body>
</html>
```